Business Card

Need business cards and small flyers for a musical band

Target Market(s)

Promoters, clients seeking to hire a Latin band

Industry/Entity Type

Business

Requirements
Must have
• The name of the band is Orchestra Brisa so want to have the background with a fire design, with black card and the name of the band in RED, maybe a combination of Red with some yellow. See attached idea.
Nice to have
• See attached files for some ideas.

```html
<!DOCTYPE html>
<html lang="en">
<head>
<meta charset="UTF-8">
<title>Orchestra Brisa – Business Card</title>
<link rel="stylesheet" href="https://fonts.googleapis.com/css2?family=Cinzel:wght@600&display=swap">
<style>
  :root {
    --card-black: #0c0203;
    --type-orange: #f7941d;
    --type-shadow: rgba(0, 0, 0, 0.85);
  }
  html, body {
    margin: 0;
    padding: 0;
    overflow: hidden;
    background: var(--card-black);
  }
  .business-card {
    position: relative;
    width: 1200px;
    height: 695px;
    overflow: hidden;
    background: var(--card-black);
    font-family: "Cinzel", "Times New Roman", serif;
    font-weight: 600;
    color: var(--type-orange);
  }
  .flame-backdrop {
    position: absolute;
    inset: 0;
    width: 100%;
    height: 100%;
  }
  .card-content {
    position: absolute;
    inset: 0;
    text-align: center;
  }
  .band-name {
    position: absolute;
    left: 0;
    right: 0;
    top: 172px;
    margin: 0;
    font-size: 76px;
    font-weight: 600;
    line-height: 1;
    letter-spacing: 3px;
  }
  .role-title {
    position: absolute;
    left: 0;
    right: 0;
    top: 330px;
    margin: 0;
    font-size: 48px;
    font-weight: 600;
    font-variant: small-caps;
    letter-spacing: 2px;
    text-shadow: -3px 3px 3px var(--type-shadow);
  }
  .contact-block {
    position: absolute;
    left: 0;
    right: 0;
    top: 508px;
    margin: 0;
    font-style: normal;
    font-size: 48px;
    font-weight: 600;
    font-variant: small-caps;
    letter-spacing: 2px;
    line-height: 57px;
    text-shadow: -3px 3px 3px var(--type-shadow);
  }
  .contact-block span {
    display: block;
  }
  .contact-email {
    text-transform: lowercase;
  }
  .contact-email .digits {
    display: inline;
    font-size: 0.8em;
  }
</style>
</head>
<body>
  <main class="business-card">
    <svg class="flame-backdrop" viewBox="0 0 1200 695" preserveAspectRatio="none" role="img" aria-label="Swirling red fire and smoke flames across a black background">
      <defs>
        <radialGradient id="glowLeft" cx="0.18" cy="0.72" r="0.55">
          <stop offset="0" stop-color="#a8151b" stop-opacity="0.85"/>
          <stop offset="0.5" stop-color="#5a0509" stop-opacity="0.6"/>
          <stop offset="1" stop-color="#0c0203" stop-opacity="0"/>
        </radialGradient>
        <radialGradient id="glowRight" cx="0.85" cy="0.3" r="0.5">
          <stop offset="0" stop-color="#9a1015" stop-opacity="0.8"/>
          <stop offset="0.55" stop-color="#4a0407" stop-opacity="0.5"/>
          <stop offset="1" stop-color="#0c0203" stop-opacity="0"/>
        </radialGradient>
        <radialGradient id="glowCenter" cx="0.55" cy="0.55" r="0.45">
          <stop offset="0" stop-color="#6e080c" stop-opacity="0.7"/>
          <stop offset="1" stop-color="#0c0203" stop-opacity="0"/>
        </radialGradient>
      </defs>
      <rect width="1200" height="695" fill="#0c0203"/>
      <rect width="1200" height="695" fill="url(#glowCenter)"/>
      <rect width="1200" height="695" fill="url(#glowLeft)"/>
      <rect width="1200" height="695" fill="url(#glowRight)"/>
    </svg>

    <div class="card-content">
      <h1 class="band-name">Orchestra Brisa</h1>
      <p class="role-title">Musical Director</p>
      <address class="contact-block">
        <span class="contact-name">Tomas Villareal</span>
        <span class="contact-email">tomasv<span class="digits">552</span>@mailbox.net</span>
        <span class="contact-phone">813-555-0148</span>
      </address>
    </div>
  </main>
</body>
</html>
```